ashby paving works

Needs to have phone number 0412885107 and email marklowry@pavemail.com.au.
ABN 27613048852
name mark lowry

For all your concreting solutions
Excavation
Exposed & colour concrete
House & shed slabs
Driveways
Landing & steps

Contact Information for Business Card

ph 0412885107
email marklowry@pavemail.com.au.
ABN 27613048852
name mark lowry

```html
<!DOCTYPE html>
<html lang="en">
<head>
<meta charset="utf-8">
<title>Ashby Paving Works – Business Card</title>
<link href="https://fonts.googleapis.com/css2?family=Hind:wght@400;500;600&family=Questrial&display=swap" rel="stylesheet">
<style>
  :root {
    --backdrop: #4b4b4d;
    --orange: #f26a21;
    --grey: #5f6062;
    --white: #ffffff;
    --card-shadow: 0 4px 10px rgba(0,0,0,0.45);
  }
  * { margin: 0; padding: 0; box-sizing: border-box; }
  html, body { width: 1200px; height: 802px; overflow: hidden; }
  body {
    background: var(--backdrop);
    font-family: "Hind", Arial, sans-serif;
    position: relative;
  }
  .card {
    position: absolute;
    top: 274px;
    width: 443px;
    height: 264px;
    background: var(--white);
    box-shadow: var(--card-shadow);
    overflow: hidden;
  }
  /* Front */
  .card--front { left: 136px; }
  .front__panel {
    position: absolute;
    left: 134px; top: 0; right: 0; bottom: 0;
    background: var(--orange);
  }
  .front__brand {
    position: absolute;
    left: 18px; top: 96px;
    width: 100px;
    display: flex; flex-direction: column; align-items: flex-start; gap: 8px;
  }
  .front__mark { width: 18px; height: 18px; background: var(--grey); }
  .front__brand-name {
    color: var(--grey);
    font-weight: 600;
    font-size: 17px;
    line-height: 1.1;
    text-transform: uppercase;
  }
  .front__details {
    position: absolute;
    right: 27px; top: 28px;
    text-align: right;
    color: var(--white);
  }
  .holder-name { font-size: 16.5px; font-weight: 600; text-transform: uppercase; line-height: 1.2; margin-bottom: 8px; }
  .contact-line { font-size: 12px; line-height: 19px; }
  .front__services {
    position: absolute;
    right: 27px; top: 170px;
    text-align: right;
    color: var(--white);
  }
  .tagline { font-size: 10.5px; text-transform: uppercase; line-height: 14px; margin-bottom: 3px; }
  .service-line { font-size: 12.5px; line-height: 16px; }
  /* Back */
  .card--back { left: 624px; }
  .back__lockup {
    position: absolute;
    left: 70px; top: 91px;
    display: flex; align-items: center;
  }
  .back__mark { width: 44px; height: 44px; background: var(--grey); margin-right: 16px; }
  .back__divider { width: 1.5px; height: 82px; background: var(--orange); margin-right: 10px; }
  .back__text { display: flex; flex-direction: column; align-items: center; }
  .back__name {
    color: var(--orange);
    font-family: "Questrial", Arial, sans-serif;
    font-size: 19px;
    font-weight: 400;
    letter-spacing: 0.5px;
    text-transform: uppercase;
  }
  .back__phone {
    color: var(--orange);
    font-family: "Questrial", Arial, sans-serif;
    font-size: 14px;
    letter-spacing: 2px;
    margin-top: 4px;
  }
</style>
</head>
<body>
  <section class="card card--front">
    <div class="front__panel"></div>
    <div class="front__brand">
      <span class="front__mark"></span>
      <span class="front__brand-name">Ashby Paving Works</span>
    </div>
    <div class="front__details">
      <p class="holder-name">Mark Lowry</p>
      <p class="contact-line">ABN 27613048852</p>
      <p class="contact-line">marklowry@pavemail.com.au</p>
    </div>
    <div class="front__services">
      <p class="tagline">For all your concreting<br>solutions</p>
      <p class="service-line">Excavation &nbsp;| Landing &amp; step</p>
      <p class="service-line">House &amp; shed slabs &nbsp;| &nbsp;Driveways</p>
      <p class="service-line">Exposed &amp; colour concrete</p>
    </div>
  </section>

  <section class="card card--back">
    <div class="back__lockup">
      <span class="back__mark"></span>
      <span class="back__divider"></span>
      <div class="back__text">
        <span class="back__name">Ashby Paving Works</span>
        <span class="back__phone">0412885107</span>
      </div>
    </div>
  </section>
</body>
</html>
```